Modern Business Card Design Needed for Young Realtor

Information that is going on the card:Marvin Pold
Broker/Owner
555.210.3367
Marvin@MPoldRealty.com
www.MPoldRealty.com

Would also like to include my Instagram Handle somewhere. Probably on the back: the_queencity_realtorMy previous business card is attached, I like that one but would like an updated version and maybe a few design changes

Marvin Pold
Broker/Owner
555.210.3367
Marvin@MPoldRealty.com
www.MPoldRealty.com

• Would also like to include my Instagram Handle somewhere. Probably on the back: the_pinecrest_realtor
• Dorrance Hale or the DH (logo from the previous card.)

```html
<!DOCTYPE html>
<html lang="en">
<head>
<meta charset="utf-8">
<title>MPold Realty – Business Card</title>
<link rel="stylesheet" href="https://fonts.googleapis.com/css2?family=EB+Garamond:wght@400&family=Roboto+Slab:wght@700&family=Work+Sans:wght@400&display=swap">
<style>
  :root {
    --brand-red: #ac1f2e;
    --paper: #ffffff;
    --ink-grey: #6b6b6b;
    --backdrop: #d4d4d4;
    --photo-light: #b89a86;
    --photo-mid: #6e5a4f;
    --photo-dark: #4a4c50;
  }
  * { box-sizing: border-box; margin: 0; padding: 0; }
  html, body {
    width: 1125px; height: 1200px; overflow: hidden;
    background: var(--backdrop);
  }
  .canvas { position: relative; width: 1125px; height: 1200px; }

  .card {
    position: absolute; left: 141px; width: 841px; height: 480px;
    border-radius: 18px; overflow: hidden;
  }
  .card--front { top: 94px; background: var(--paper); }
  .card--back  { top: 625px; background: var(--brand-red); }

  .wordmark {
    font-family: "EB Garamond", "Times New Roman", serif; font-weight: 400;
    text-transform: uppercase; white-space: nowrap; line-height: 1;
  }
  .card--front .wordmark {
    position: absolute; left: 37px; top: 76px;
    font-size: 40px; letter-spacing: 4px; color: var(--brand-red);
  }

  .name-band {
    position: absolute; left: 0; top: 221px; width: 100%; height: 80px;
    background: var(--brand-red); color: var(--paper);
    padding: 10px 0 0 37px;
  }
  .agent-name {
    font-family: "Roboto Slab", Georgia, serif; font-weight: 700;
    font-size: 27px; line-height: 34px;
  }
  .agent-title {
    font-family: "Work Sans", sans-serif; font-size: 17px; line-height: 24px;
    letter-spacing: 0.3px;
  }

  .agent-photo {
    position: absolute; left: 430px; top: 94px; width: 411px; height: 386px;
    border-radius: 200px 160px 0 0;
    background: linear-gradient(180deg, var(--photo-mid) 0%, var(--photo-light) 45%, var(--photo-dark) 100%);
  }

  .contact-list {
    position: absolute; left: 37px; top: 350px; list-style: none;
    font-family: "Work Sans", sans-serif; font-size: 18px; color: var(--ink-grey);
  }
  .contact-item { display: flex; align-items: center; height: 29px; white-space: nowrap; }
  .contact-icon { width: 13px; height: 13px; margin-right: 11px; fill: var(--brand-red); flex: none; }

  .card--back .wordmark {
    position: absolute; left: 0; right: 0; top: 238px; text-align: center;
    font-size: 50px; letter-spacing: 8px; color: var(--paper);
    padding-left: 8px;
  }
  .social-handle {
    position: absolute; left: 0; right: 0; top: 424px;
    display: flex; justify-content: center; align-items: center;
    font-family: "Work Sans", sans-serif; font-size: 18px; line-height: 24px; color: var(--paper);
  }
  .social-dot {
    width: 15px; height: 15px; border-radius: 50%;
    border: 2px solid var(--paper); margin-right: 9px; flex: none;
  }
</style>
</head>
<body>
<main class="canvas">
  <section class="card card--front">
    <div class="wordmark">MPold Realty</div>

    <div class="name-band">
      <h1 class="agent-name">Marvin Pold</h1>
      <p class="agent-title">Broker/Owner</p>
    </div>

    <div class="agent-photo" role="img" aria-label="Portrait photo of the broker in a grey blazer and white shirt"></div>

    <ul class="contact-list">
      <li class="contact-item">
        <svg class="contact-icon" viewBox="0 0 16 16" aria-hidden="true"><path d="M3.5 1 6 3.5 4.6 5.6c.9 2 2.7 3.8 4.8 4.8L11.5 9 14 11.5 12.2 14C6.6 13.6 1.4 8.4 1 2.8z"/></svg>
        555.210.3367
      </li>
      <li class="contact-item">
        <svg class="contact-icon" viewBox="0 0 16 16" aria-hidden="true"><path d="M1 3h14v10H1zm2 2v6h10V5L8 8.5z"/></svg>
        Marvin@MPoldRealty.com
      </li>
      <li class="contact-item">
        <svg class="contact-icon" viewBox="0 0 16 16" aria-hidden="true"><circle cx="8" cy="8" r="7"/><path d="M8 1v14M1 8h14" stroke="#fff" stroke-width="1.2"/></svg>
        www.MPoldRealty.com
      </li>
    </ul>
  </section>

  <section class="card card--back">
    <div class="wordmark">MPold Realty</div>
    <p class="social-handle"><span class="social-dot" aria-hidden="true"></span>@the_pinecrest_realtor</p>
  </section>
</main>
</body>
</html>
```